Real Estate Website

I am looking for a website design for a website that will be featuring real estate listings across Australia. It will be a website for a real estate agency that operates through all states in Australia.

We like the designs of https://www.brightharbourhomes.com.au/ and https://velmora.asia/

On the lifestyle website, we like the sell, buy, sold tabs but would also like lease, and agents. We also need a button somewhere for 'Join Agent Pallisto' and 'Login'

On the Velmora site it has a concierge section and we want something like that on the home page.

The contact details to show in the footer are:

Shop 2174B
Level 1 Tidewater Plaza Shopping Centre
87 Quarry Lane
Southport

Attached are various versions of the logo and some intro text to go on the home page.

```html
<!DOCTYPE html>
<html lang="en">
<head>
<meta charset="utf-8">
<title>Agent Pallisto</title>
<link href="https://fonts.googleapis.com/css2?family=Inter:wght@400;500;600;700;800&family=Roboto:wght@500&display=swap" rel="stylesheet">
<style>
:root{
  --gold:#c6a26e;
  --brown:#7d5a2a;
  --tan:#c8a676;
  --ink:#111111;
  --black:#000000;
  --white:#ffffff;
  --muted:#444;
  --line:#d9d9d9;
}
*{box-sizing:border-box;margin:0;padding:0}
html,body{width:1200px;height:3265px;overflow:hidden}
body{position:relative;font-family:'Inter',sans-serif;color:var(--ink);background:var(--white)}
.abs{position:absolute}
/* hero */
.hero{left:0;top:0;width:1200px;height:598px;background:linear-gradient(180deg,#4d4a4c 0%,#6e5b4a 35%,#3d3a36 65%,#1e1f22 100%)}
.brand{left:114px;top:50px;display:flex;align-items:center;gap:10px;color:var(--white);font-size:20px;font-weight:600}
.brand .dot{width:12px;height:12px;border-radius:50%;background:var(--white)}
.nav{top:52px;left:388px;display:flex;gap:27px;font-size:16px;font-weight:500;color:var(--white)}
.nav .active{color:var(--gold)}
.btn-pill{display:flex;align-items:center;justify-content:center;background:var(--brown);color:var(--white);font-size:15px;font-weight:500;border-radius:14px 0 14px 0}
.join{left:796px;top:39px;width:162px;height:47px}
.login{left:982px;top:39px;width:108px;height:47px}
.tabs{left:310px;top:283px;display:flex;gap:3px}
.tab{width:80px;height:44px;border-radius:16px 16px 0 0;background:var(--tan);color:var(--white);font-size:16px;font-weight:500;display:flex;align-items:center;justify-content:center}
.tab.on{background:var(--brown)}
.search{left:310px;top:327px;width:412px;height:48px;background:var(--white);font-size:12px;color:#333;padding:0 16px;display:flex;align-items:center}
.find{left:722px;top:327px;width:167px;height:48px;background:var(--tan);font-size:15px;font-weight:600;color:var(--ink);display:flex;align-items:center;justify-content:center;gap:7px}
/* categories */
.cat{top:672px;width:319px;height:272px}
.cat-label{top:907px;width:293px;height:60px;background:var(--white);box-shadow:0 4px 10px rgba(0,0,0,.15);font-family:'Roboto',sans-serif;font-size:26px;font-weight:500;display:flex;align-items:center;justify-content:center}
.cat-label.on{background:var(--brown);color:var(--white)}
/* featured */
.section-title{left:0;width:1200px;text-align:center;font-size:30px;font-weight:700;letter-spacing:.3px}
.card{top:1188px;width:311px;height:405px;border:2px solid #e2e2e2;border-radius:12px;overflow:hidden;background:var(--white);text-align:center}
.card .ph{height:228px}
.card h3{font-size:21px;font-weight:500;margin-top:14px}
.card p{font-size:16px;color:#333;line-height:26px;margin:6px 20px 0}
.card .price{margin:12px 18px 0;font-size:16px;font-weight:500;display:flex;align-items:center;gap:10px}
.card .price::before,.card .price::after{content:"";flex:1;height:1px;background:var(--line)}
.card .specs{font-size:13px;color:var(--gold);margin-top:16px}
.arrow{width:34px;height:34px;border-radius:50%;background:var(--white);box-shadow:0 2px 8px rgba(0,0,0,.2);display:flex;align-items:center;justify-content:center}
/* about */
.about{left:0;top:1661px;width:1200px;height:711px;background:var(--black)}
.about-box{left:568px;top:1809px;width:534px;height:418px;background:var(--white);padding:48px 30px 0}
.about-box h2{font-size:30px;font-weight:800}
.about-box p{font-size:14px;line-height:25.6px;color:#444;margin-top:10px}
.about-box p+p{margin-top:8px}
.readmore{left:600px;top:2151px;width:165px;height:48px}
/* concierge */
.concierge{left:0;top:2372px;width:1200px;height:457px;background:var(--tan);text-align:center}
.concierge h2{position:absolute;top:150px;width:100%;font-size:37px;font-weight:400}
.concierge h2 b{font-weight:800}
.concierge p{position:absolute;top:225px;left:160px;width:880px;font-size:18px;line-height:25.5px;color:#1a1a1a}
.find-more{left:517px;top:2703px;width:166px;height:47px}
/* footer */
.footer{left:0;top:2829px;width:1200px;height:380px;background:var(--ink);color:var(--white)}
.foot-brand{left:105px;top:3090px;font-size:28px;font-weight:600;color:var(--white)}
.foot-col{top:2940px}
.foot-col h4{font-size:18px;font-weight:600;margin-bottom:22px}
.foot-col li{list-style:none;font-size:16px;line-height:32.5px;padding-left:2px}
.contact-row{display:flex;gap:12px;font-size:14.5px;line-height:25.5px;margin-bottom:13px}
.contact-row svg{flex:none;margin-top:6px}
.bottom{left:0;top:3209px;width:1200px;height:56px;background:var(--brown);color:var(--white);font-size:16px;display:flex;align-items:center;justify-content:center}
</style>
</head>
<body>

<header>
  <div class="abs hero" role="img" aria-label="Evening city skyline with river and arched bridge"></div>
  <div class="abs brand"><span class="dot"></span>Agent Pallisto</div>
  <nav class="abs nav"><span class="active">Home</span><span>Sell</span><span>Buy</span><span>Sold</span><span>Lease</span><span>Agents</span></nav>
  <div class="abs btn-pill join">Join Agent Pallisto</div>
  <div class="abs btn-pill login">Login</div>
  <div class="abs tabs"><div class="tab on">Sell</div><div class="tab">Buy</div><div class="tab">Sold</div></div>
  <div class="abs search">Start typing to find your Addresss</div>
  <div class="abs find">Find Out
    <svg width="13" height="13" viewBox="0 0 14 14"><circle cx="7" cy="7" r="7" fill="#111"/><path d="M5.5 4l3 3-3 3" stroke="#c8a676" stroke-width="1.8" fill="none"/></svg>
  </div>
</header>

<section class="categories">
  <div class="abs cat" style="left:110px;background:linear-gradient(180deg,#6d7a92,#4a5566 55%,#4e6b3a)" role="img" aria-label="Two-storey blue house with lit porch"></div>
  <div class="abs cat" style="left:440px;background:linear-gradient(180deg,#b9c7cf,#8b3a3a 55%,#c9c1b0)" role="img" aria-label="Happy couple receiving house keys"></div>
  <div class="abs cat" style="left:769px;background:linear-gradient(180deg,#8a7a68,#c9bba6 55%,#6b5744)" role="img" aria-label="Warm modern living room interior"></div>
  <div class="abs cat-label" style="left:125px">Sell</div>
  <div class="abs cat-label on" style="left:455px">Buy</div>
  <div class="abs cat-label" style="left:784px">Sold</div>
</section>

<section class="featured">
  <h2 class="abs section-title" style="top:1110px">FEATURED PROPERTIES</h2>

  <article class="abs card" style="left:99px">
    <div class="ph" style="background:linear-gradient(135deg,#e6e6e4,#9aa4b0 60%,#2f3542)" role="img" aria-label="Agent presenting a model house to a client"></div>
    <h3>Agents</h3><p>3120 Lorem ipsum dolor sit adipiscing 89121</p>
    <div class="price">Price: $320,000</div>
    <div class="specs">3,530 Sq.fit · 4 Bed · 3 &nbsp;Bath · 3 Garage</div>
  </article>
  <article class="abs card" style="left:445px">
    <div class="ph" style="background:linear-gradient(135deg,#f1f1ef,#d8d6d2 55%,#7a3f6a)" role="img" aria-label="Agent handing keys to a couple in a kitchen"></div>
    <h3>Buy</h3><p>3120 Lorem ipsum dolor sit adipiscing 89121</p>
    <div class="price">Price: $320,000</div>
    <div class="specs">3,530 Sq.fit · 4 Bed · 3 &nbsp;Bath · 3 Garage</div>
  </article>
  <article class="abs card" style="left:789px">
    <div class="ph" style="background:linear-gradient(180deg,#8fb6de,#6f7c86 50%,#5b8a3e 75%,#8a8a8a)" role="img" aria-label="Row of suburban villas along a street"></div>
    <h3>Villa</h3><p>3120 Lorem ipsum dolor sit adipiscing 89121</p>
    <div class="price">Price: $320,000</div>
    <div class="specs">3,530 Sq.fit · 4 Bed · 3 &nbsp;Bath · 3 Garage</div>
  </article>

  <div class="abs arrow" style="left:79px;top:1391px"><svg width="12" height="12" viewBox="0 0 12 12"><path d="M8 1L3 6l5 5" stroke="#1d3a6b" stroke-width="2" fill="none"/></svg></div>
  <div class="abs arrow" style="left:1083px;top:1391px"><svg width="12" height="12" viewBox="0 0 12 12"><path d="M4 1l5 5-5 5" stroke="#1d3a6b" stroke-width="2" fill="none"/></svg></div>
</section>

<section>
  <div class="abs about"></div>
  <div class="abs" style="left:51px;top:1720px;width:81px;height:80px;background:rgba(198,162,110,.35)" role="img" aria-label="Decorative gold dot pattern"></div>
  <div class="abs" style="left:101px;top:1752px;width:564px;height:534px;background:linear-gradient(160deg,#6b4a32,#3d4a44 45%,#7e8f6a 80%,#5a6b3a)" role="img" aria-label="Couple embracing in front of a modern home"></div>
  <div class="abs about-box">
    <h2>ABOUT US</h2>
    <p>Sed ut perspiciatis unde omnis iste natus error sit voluptatem accusantium doloremque laudantium, totam rem aperiam, eaque ipsa quae ab illo inventore veritatis et quasi architecto beatae vitae dicta sunt explicabo. Nemo enim ipsam voluptatem quia voluptas sit aspernatur aut odit aut fugit, sed quia consequuntur magni dolores eos qui ratione voluptatem sequi nesciunt.</p>
    <p>Sed ut perspiciatis unde omnis iste natus error sit voluptatem accusantium doloremque laudantium</p>
  </div>
  <div class="abs btn-pill readmore">Read More&nbsp;
    <svg width="13" height="13" viewBox="0 0 14 14"><circle cx="7" cy="7" r="7" fill="#fff"/><path d="M5.5 4l3 3-3 3" stroke="#7d5a2a" stroke-width="1.8" fill="none"/></svg>
  </div>
</section>

<section class="abs concierge">
  <h2>AGENT PALLISTO <b>CONCIERGE</b></h2>
  <p>Lorem ipsum dolor sit amet, consectetur adipiscing elit, sed do eiusmod tempor incididunt ut labore et Lorem ipsum dolor sit amet, consectetur adipiscing elit, sed do eiusmod tempor incididunt ut labore et Lorem ipsum dolor sit amet, consectetur adipiscing elit, sed do</p>
</section>
<div class="abs btn-pill find-more">Find out More&nbsp;
  <svg width="13" height="13" viewBox="0 0 14 14"><circle cx="7" cy="7" r="7" fill="#fff"/><path d="M5.5 4l3 3-3 3" stroke="#7d5a2a" stroke-width="1.8" fill="none"/></svg>
</div>

<footer>
  <div class="abs footer"></div>
  <div class="abs foot-brand">Agent Pallisto</div>
  <div class="abs foot-col" style="left:517px;color:#fff">
    <h4>QUICK LINK</h4>
    <ul><li>Sell</li><li>Buy</li><li>Sold</li><li>Lease</li><li>Agents</li></ul>
  </div>
  <div class="abs foot-col" style="left:699px;width:250px;color:#fff">
    <h4>CONTACT</h4>
    <div class="contact-row"><svg width="11" height="14" viewBox="0 0 11 14"><path d="M5.5 0A5.5 5.5 0 0 0 0 5.5C0 9.5 5.5 14 5.5 14S11 9.5 11 5.5A5.5 5.5 0 0 0 5.5 0zm0 7.6a2.1 2.1 0 1 1 0-4.2 2.1 2.1 0 0 1 0 4.2z" fill="#fff"/></svg><span>Shop 2174BLevel 1 Tidewater Plaza Shopping Centre 87 Quarry Lane Southport</span></div>
    <div class="contact-row"><svg width="13" height="13" viewBox="0 0 13 13"><path d="M3 .5l2 2.6-1.2 1.6a7 7 0 0 0 4.5 4.5l1.6-1.2 2.6 2L11.8 12C6 12.5.5 7 1 1.2z" fill="#fff"/></svg><span>+61 7 5550 1482</span></div>
    <div class="contact-row"><svg width="15" height="12" viewBox="0 0 15 12"><rect x=".7" y=".7" width="13.6" height="10.6" rx="1" fill="none" stroke="#fff" stroke-width="1.3"/><path d="M1 1.5l6.5 5 6.5-5" fill="none" stroke="#fff" stroke-width="1.3"/></svg><span>info@agentpallisto.com</span></div>
  </div>
  <div class="abs foot-col" style="left:959px;color:#fff">
    <h4>HELP LINK</h4>
    <ul><li>Terms&amp;condtions</li><li>Privacy Policy</li><li>About Us</li><li>Support</li></ul>
  </div>
  <div class="abs bottom">© copyrights 2025 Agent Pallisto | &nbsp;All Rights Reserved</div>
</footer>

</body>
</html>
```